Visitenkarten für Erstellung von Beleihungswert- und Verkehrswertgutachten.
Zielgruppe
Ich erstelle Beleihungswert- und Verkehrswertgutachten.
Meine Zielgruppe sind alle Immobilieneigentümer, Kaufinteressenten, Erben von Immobilienvermögen evtl. auch Anwälte, Steuerberater.
Aufgabenstellung
Der Fokus liegt auf der Wertermittlung von Immobilien

```html
<!DOCTYPE html>
<html lang="de">
<head>
<meta charset="utf-8">
<title>Varen Immobilien Bewertung – Visitenkarten</title>
<link rel="stylesheet" href="https://fonts.googleapis.com/css2?family=Ubuntu:wght@400;500;700&display=swap">
<style>
  :root {
    --board: #f5f5f5;
    --paper: #ffffff;
    --slate: #5f6062;
    --ink: #1c1c1c;
    --text-grey: #58585a;
    --gold: #c9a55a;
    --gold-dark: #9c6d22;
    --gold-light: #d8b468;
  }
  * { box-sizing: border-box; margin: 0; padding: 0; }
  html, body { width: 814px; height: 1200px; overflow: hidden; }
  body {
    background: var(--board);
    font-family: "Ubuntu", sans-serif;
    position: relative;
  }
  .brand-block {
    position: absolute;
    left: 0; width: 814px;
    top: 120px;
    text-align: center;
    color: var(--text-grey);
    font-weight: 500;
  }
  .brand-mark {
    display: block;
    width: 22px; height: 22px;
    margin: 0 auto 14px;
    background: var(--text-grey);
  }
  .brand-name {
    font-size: 23px;
    letter-spacing: 1.2px;
  }
  .card {
    position: absolute;
    top: 264px;
    width: 358px; height: 231px;
    box-shadow: 6px 10px 14px rgba(0,0,0,0.22);
    overflow: hidden;
  }
  .card--front { left: 36px; background: var(--paper); }
  .card--back { left: 418px; background: var(--slate); }
  .card-brand {
    position: absolute;
    left: 0; width: 100%;
    text-align: center;
    font-weight: 500;
  }
  .card--front .card-brand { top: 64px; color: var(--text-grey); }
  .card--back .card-brand { top: 82px; color: var(--gold); }
  .card-brand .brand-mark { width: 16px; height: 16px; margin-bottom: 10px; }
  .card--front .brand-mark { background: var(--text-grey); }
  .card--back .brand-mark { background: var(--gold); }
  .card--front .card-brand .brand-name { font-size: 15px; letter-spacing: 0.8px; }
  .card--back .card-brand .brand-name { font-size: 18px; letter-spacing: 0.9px; }
  .holder {
    position: absolute;
    left: 142px; top: 118px;
    font-size: 12.5px;
    font-weight: 700;
    color: var(--ink);
  }
  .contact {
    position: absolute;
    left: 142px;
    font-size: 10px;
    line-height: 12px;
    color: var(--ink);
    list-style: none;
  }
  .contact li { position: relative; padding-left: 16px; }
  .contact svg { position: absolute; left: 0; top: 1px; }
  .contact--address { top: 150px; }
  .contact--reach { top: 186px; }
  .gold-band {
    position: absolute;
    left: 0; bottom: 0;
    width: 100%; height: 12px;
    background: linear-gradient(90deg, var(--gold-dark) 0%, var(--gold-light) 50%, var(--gold-dark) 100%);
  }
</style>
</head>
<body>
  <header class="brand-block">
    <span class="brand-mark"></span>
    <div class="brand-name">Varen Immobilien Bewertung</div>
  </header>

  <section class="card card--front" aria-label="Visitenkarte Vorderseite">
    <div class="card-brand">
      <span class="brand-mark"></span>
      <div class="brand-name">Varen Immobilien Bewertung</div>
    </div>
    <p class="holder">Marlene Hoff</p>
    <ul class="contact contact--address">
      <li>
        <svg width="10" height="12" viewBox="0 0 10 12"><path d="M5 0.5a4 4 0 0 1 4 4c0 3-4 7-4 7s-4-4-4-7a4 4 0 0 1 4-4z" fill="var(--gold-dark)"/><circle cx="5" cy="4.5" r="1.5" fill="#fff"/></svg>
        Lindenhofstraße 14<br>70000 Musterstadt
      </li>
    </ul>
    <ul class="contact contact--reach">
      <li>
        <svg width="12" height="12" viewBox="0 0 12 12"><rect x="0.8" y="2" width="5" height="9" rx="0.8" fill="none" stroke="var(--gold-dark)" stroke-width="1.2"/><circle cx="8.5" cy="3" r="3" fill="var(--gold-dark)"/></svg>
        0170 - 5550123
      </li>
      <li>
        <svg width="12" height="10" viewBox="0 0 12 10"><rect x="0" y="1.5" width="11" height="7.5" fill="var(--gold-dark)"/><path d="M0 1.5l5.5 4 5.5-4" fill="none" stroke="#fff" stroke-width="1"/></svg>
        info@beispiel-mail.de
      </li>
    </ul>
    <div class="gold-band"></div>
  </section>

  <section class="card card--back" aria-label="Visitenkarte Rückseite">
    <div class="card-brand">
      <span class="brand-mark"></span>
      <div class="brand-name">Varen Immobilien Bewertung</div>
    </div>
  </section>
</body>
</html>
```